Dust N Gone! Cleaning needs a flyer!

We have started a cleaning business DUST N GONE! Cleaning, and had a new logo design for it.
We would like a flyer designed to present to businesses that represents our professionalism, quality of service, security and value for money.
We would like a flyer that we can present to both our residential clients and business owners alike.
We will use this flyer for the next 2 years without having to make changes.
I'm happy for the designer to come up with their own wording if necessary.
Updates

Hello everyone!

In addition to the information I have already provided, please see below for more information to be included on the design for our flyer.

Thank you in advance.

Don’t read this unless your current cleaners are AMAZING!

Are you still reading? Now for the good news! Announcing the arrival of the amazing cleaning team of Dust N Gone! Cleaning. They’re the BEST in the Wimmera and we personally guarantee it.

We offer an ultimate service that NO other cleaning company in the Wimmera can offer; high quality cleaning of your home or business, carpet dry cleaning and pest control. All of these services can be completed at a time that is most convenient to you.

From wiping benches to washing windows, from dusting skirting boards to dry cleaning your carpets, from bathrooms to bugs, we really are your ONE stop shop.

Why choose the greatest cleaning company in the Wimmera?

For over 18 years, we have built a reputation on honesty and trust in the residential and commercial services. Our business is to know what people expect when we walk in to your home or business.

With our vast experience and knowledge, we know how to find the best people for the job, how to identify the best products for the clean, we use the newest of technology and equipment and have the best attitudes in town.

Local people, local business that you can rely on because we are also Dust N Gone! Pest Control & Fibrela all rolled in to your ONE stop shop for residential services.

Call us to discuss how we can give you the quality you demand.

Residential Cleaning                                                       Commercial Cleaning                                     

General house cleaning                                                  Business Premises          

Home help                                                                         Vacated properties

Rental vacancies                                                               Schools

Post renovation cleans                                                     Motels/Hotels

 

                                   

Target Market(s)

Business owners, commercial properties, home owners (women aged between 30 - 80y/o)

Industry/Entity Type

Residential

Requirements
Must have
• Incorporate our logo and colours.
Double sided.
Images of interiors of both home & office.
Catch phrase: "You demand quality ..... we guarantee it!"
Address: 22-26 Wattlegum St, Horsham VIC 3400
Phone: 1300 482 316
ABN: 47 308 562 194
We complete the ususal cleaning such as:
General House cleaning
Commercial Cleaning
Rental Properties
Business Premises
Other services we offer is:
Carpet dry cleaning
Upholstery cleaning
Dust N Gone! Mite Chasers pest control
Window cleaning.

```html
<!DOCTYPE html>
<html lang="en">
<head>
<meta charset="utf-8">
<title>Dust N Gone! Cleaning – Flyer</title>
<link rel="stylesheet" href="https://fonts.googleapis.com/css2?family=Didact+Gothic&family=Varela+Round&family=Nunito:wght@700;800;900&display=swap">
<style>
  :root {
    --magenta: #c8169c;
    --magenta-mid: #a20c82;
    --magenta-deep: #7d0562;
    --magenta-dark: #5a0347;
    --pink: #e457cc;
    --pink-soft: #f7c4ec;
    --pink-pale: #fdeefa;
    --yellow: #ffe600;
    --white: #ffffff;
    --ink: #1e0a18;
  }
  * { box-sizing: border-box; margin: 0; padding: 0; }
  html, body { width: 1200px; height: 845px; overflow: hidden; background: var(--white); }
  body { position: relative; font-family: "Didact Gothic", sans-serif; }

  .page { position: absolute; top: 10px; width: 587px; height: 826px; overflow: hidden; }
  .page--front { left: 11px; background: var(--magenta-dark); }
  .page--back { left: 604px; background: linear-gradient(180deg, var(--white) 50%, var(--pink-pale) 78%, #fbe0f5 100%); }

  .photo { position: absolute; left: 0; width: 100%; }
  .photo--vacuum {
    top: 0; height: 345px;
    background:
      radial-gradient(ellipse 260px 180px at 30% 40%, rgba(255,255,255,0.75), rgba(255,255,255,0) 70%),
      radial-gradient(ellipse 300px 120px at 35% 78%, rgba(150,20,120,0.55), rgba(150,20,120,0) 70%),
      linear-gradient(165deg, #fbe4f6 0%, #f4b5e6 40%, #e07bd0 75%, #c53fb2 100%);
  }
  .photo--interiors {
    top: 315px; height: 250px;
    background:
      radial-gradient(ellipse 140px 110px at 22% 55%, rgba(255,240,200,0.8), rgba(255,240,200,0) 70%),
      radial-gradient(ellipse 160px 90px at 75% 35%, rgba(250,240,70,0.9), rgba(250,240,70,0) 70%),
      linear-gradient(100deg, #d98a45 0%, #f1c27e 22%, #f4ead8 45%, #ece9e2 58%, #f0e660 75%, #dcdcdc 100%);
  }
  .photo--lounge {
    top: 0; height: 440px;
    background:
      radial-gradient(ellipse 200px 120px at 55% 70%, rgba(255,255,255,0.85), rgba(255,255,255,0) 70%),
      radial-gradient(ellipse 120px 140px at 30% 20%, rgba(255,255,255,0.7), rgba(255,255,255,0) 70%),
      radial-gradient(ellipse 180px 90px at 85% 72%, rgba(170,20,140,0.7), rgba(170,20,140,0) 70%),
      linear-gradient(170deg, #f6b7ec 0%, #ea7ddc 40%, #d748c6 70%, #c22db0 100%);
  }

  .shape { position: absolute; left: 0; width: 100%; display: block; }

  .brand { position: absolute; display: flex; align-items: flex-start; gap: 8px; }
  .brand__mark { width: 13px; height: 13px; margin-top: 6px; background: currentColor; flex: none; }
  .brand__name { font-family: "Varela Round", sans-serif; font-size: 23px; line-height: 1.05; letter-spacing: 0.5px; white-space: nowrap; }
  .brand__contact { font-size: 10px; margin-top: 7px; letter-spacing: 0.3px; white-space: nowrap; }
  .page--front .brand { top: 74px; left: 342px; color: var(--magenta); }
  .page--front .brand__contact { color: var(--magenta-deep); }
  .page--back .brand { top: 130px; left: 338px; color: var(--white); }

  .catchphrase { position: absolute; top: 262px; left: 112px; transform: rotate(-5deg); transform-origin: left top; font-family: "Nunito", sans-serif; font-weight: 900; line-height: 0.95; white-space: nowrap; }
  .catchphrase__lead { display: block; font-size: 32px; color: var(--yellow); text-shadow: 2px 2px 0 var(--magenta), -1px -1px 0 var(--magenta), 1px -1px 0 var(--magenta), -1px 1px 0 var(--magenta); }
  .catchphrase__tail { display: block; margin-left: 68px; font-size: 48px; color: var(--white); text-shadow: 2px 2px 0 var(--magenta), -1px -1px 0 var(--magenta), 1px -1px 0 var(--magenta), -1px 1px 0 var(--magenta); }

  .details { position: absolute; top: 578px; left: 0; width: 100%; text-align: center; color: var(--white); font-family: "Varela Round", sans-serif; }
  .details__address { font-size: 20px; text-align: left; padding-left: 72px; white-space: nowrap; }
  .details__phone { font-size: 18.5px; text-align: left; padding-left: 72px; margin-top: 3px; white-space: nowrap; }
  .details__phone b { font-weight: normal; color: var(--yellow); }
  .details__sep { display: inline-block; width: 1px; height: 18px; background: rgba(255,255,255,0.6); margin: 0 12px; vertical-align: -3px; }
  .details__intro { font-size: 17px; margin: 12px auto 5px; padding-bottom: 3px; width: 400px; border-bottom: 1px solid rgba(255,255,255,0.5); white-space: nowrap; }
  .service-grid { display: grid; grid-template-columns: 1fr 1fr; width: 540px; margin: 0 auto; font-size: 15px; color: var(--yellow); line-height: 1.15; white-space: nowrap; }
  .service-grid span:nth-child(odd) { text-align: right; padding-right: 9px; border-right: 1px solid rgba(255,255,255,0.6); }
  .service-grid span:nth-child(even) { text-align: left; padding-left: 9px; }
  .details__other { font-size: 13.5px; margin: 13px auto 6px; padding-bottom: 3px; width: 250px; border-bottom: 1px solid rgba(255,255,255,0.5); }
  .service-row { font-size: 13.5px; color: var(--yellow); white-space: nowrap; }
  .service-row span + span { border-left: 1px solid rgba(255,255,255,0.6); margin-left: 6px; padding-left: 6px; }
  .pest { font-size: 20px; margin-top: 12px; font-weight: 800; font-family: "Nunito", sans-serif; white-space: nowrap; }
  .pest b { color: var(--yellow); }

  .headline { position: absolute; top: 36px; right: 36px; text-align: right; font-family: "Nunito", sans-serif; font-weight: 900; color: var(--yellow); font-size: 27px; line-height: 1.05; white-space: nowrap; text-shadow: 2px 2px 0 var(--magenta), -1px -1px 0 var(--magenta), 1px -1px 0 var(--magenta), -1px 1px 0 var(--magenta); }
  .headline span { display: block; }
  .headline span:first-child { margin-right: 118px; }

  .copy { position: absolute; top: 432px; left: 62px; width: 465px; text-align: center; color: var(--ink); font-size: 10.4px; line-height: 1.18; }
  .copy h2 { font-family: "Nunito", sans-serif; font-weight: 800; font-size: 12.5px; margin-bottom: 8px; }
  .copy p { margin-bottom: 10px; }
  .copy .call { font-family: "Nunito", sans-serif; font-weight: 800; font-size: 14px; margin: 4px 0 8px; white-space: nowrap; }
  .lists { display: flex; justify-content: center; gap: 70px; text-align: left; font-family: "Nunito", sans-serif; font-weight: 700; font-size: 11.5px; line-height: 1.15; }
  .lists h3 { font-size: 11px; font-weight: 800; text-decoration: underline; margin-bottom: 3px; }
  .lists ul { list-style: none; }
</style>
</head>
<body>

  <section class="page page--front">
    <div class="photo photo--vacuum" role="img" aria-label="Cleaner vacuuming a carpet in a bright room"></div>
    <div class="photo photo--interiors" role="img" aria-label="Home lounge and modern office interiors"></div>

    <svg class="shape" style="top:200px" width="587" height="170" viewBox="0 0 587 170" aria-hidden="true">
      <defs>
        <linearGradient id="frontBand" x1="0" y1="0" x2="1" y2="0">
          <stop offset="0" stop-color="#d84cc2"/>
          <stop offset="0.6" stop-color="#e772d4"/>
          <stop offset="1" stop-color="#f3b2e6" stop-opacity="0.6"/>
        </linearGradient>
      </defs>
      <path d="M0 60 C180 45 380 20 587 0 L587 90 C400 100 200 120 0 160 Z" fill="url(#frontBand)"/>
      <path d="M0 160 C200 120 400 100 587 90 L587 96 C400 108 200 128 0 168 Z" fill="#ffffff" opacity="0.8"/>
    </svg>

    <svg class="shape" style="top:500px" width="587" height="326" viewBox="0 0 587 326" aria-hidden="true">
      <defs>
        <linearGradient id="frontBase" x1="0" y1="0" x2="0" y2="1">
          <stop offset="0" stop-color="#c8169c"/>
          <stop offset="0.5" stop-color="#a20c82"/>
          <stop offset="1" stop-color="#5a0347"/>
        </linearGradient>
      </defs>
      <path d="M0 40 C200 5 400 -5 587 25 L587 326 L0 326 Z" fill="url(#frontBase)"/>
      <path d="M0 40 C200 5 400 -5 587 25" fill="none" stroke="#f7b6ea" stroke-width="2.5"/>
    </svg>

    <div class="brand">
      <span class="brand__mark"></span>
      <div>
        <div class="brand__name">DUST N GONE!<br>CLEANING</div>
        <div class="brand__contact">P. 1300 482 316 &nbsp;F. 03 5391 7604</div>
      </div>
    </div>

    <div class="catchphrase">
      <span class="catchphrase__lead">You demand quality...</span>
      <span class="catchphrase__tail">we guarantee it!</span>
    </div>

    <div class="details">
      <p class="details__address">22-26 Wattlegum St, Horsham VIC 3400</p>
      <p class="details__phone"><b>Phone:</b> 1300 482 316<span class="details__sep"></span><b>ABN:</b> 47 308 562 194</p>
      <p class="details__intro">We complete the ususal cleaning such as:</p>
      <div class="service-grid">
        <span>GENERAL HOUSE CLEANING</span><span>COMMERCIAL CLEANING</span>
        <span>RENTAL PROPERTIES</span><span>BUSINESS PREMISES</span>
      </div>
      <p class="details__other">Other services we offer is:</p>
      <p class="service-row"><span>CARPET DRY CLEANING</span><span>UPHOLSTERY CLEANING</span><span>WINDOW CLEANING</span></p>
      <p class="pest"><b>DUST N GONE!</b> Mite Chasers pest control</p>
    </div>
  </section>

  <section class="page page--back">
    <div class="photo photo--lounge" role="img" aria-label="Bright modern living room with sofa, coffee table and rug"></div>

    <svg class="shape" style="top:0" width="587" height="460" viewBox="0 0 587 460" aria-hidden="true">
      <defs>
        <linearGradient id="backSweep" x1="0" y1="0" x2="1" y2="1">
          <stop offset="0" stop-color="#ffffff"/>
          <stop offset="1" stop-color="#fbe6f7"/>
        </linearGradient>
      </defs>
      <path d="M0 0 L62 0 C20 110 30 260 150 360 C250 430 420 425 587 405 L587 460 L0 460 Z" fill="url(#backSweep)"/>
      <path d="M62 0 C20 110 30 260 150 360 C250 430 420 425 587 405" fill="none" stroke="#f3b3e6" stroke-width="5"/>
    </svg>

    <h1 class="headline"><span>You will experience</span><span>a new level of clean!</span></h1>

    <div class="brand">
      <span class="brand__mark"></span>
      <div>
        <div class="brand__name">DUST N GONE!<br>CLEANING</div>
        <div class="brand__contact">P. 1300 482 316 &nbsp;F. 03 5391 7604</div>
      </div>
    </div>

    <div class="copy">
      <h2>Don’t read this unless your current cleaners are AMAZING!</h2>
      <p>Are you still reading? Now for the good news! Announcing the arrival of the amazing cleaning team of Dust N Gone! Cleaning. They’re the BEST in the Wimmera and we personally guarantee it.</p>
      <p>We offer an ultimate service that NO other cleaning company in the Wimmera can offer; high quality cleaning of your home or business, carpet dry cleaning and pest control. All of these services can be completed at a time that is most convenient to you.</p>
      <p>From wiping benches to washing windows, from dusting skirting boards to dry cleaning your carpets, from bathrooms to bugs, we really are your ONE stop shop.</p>
      <h2>Why choose the greatest cleaning company in the Wimmera?</h2>
      <p>For over 18 years, we have built a reputation on honesty and trust in the residential and commercial services. Our business is to know what people expect when we walk in to your home or business.</p>
      <p>With our vast experience and knowledge, we know how to find the best people for the job, how to identify the best products for the clean, we use the newest of technology and equipment and have the best attitudes in town.</p>
      <p>Local people, local business that you can rely on because we are also Dust N Gone! Pest Control &amp; Fibrela all rolled in to your ONE stop shop for residential services.</p>
      <p class="call">Call us to discuss how we can give you the quality you demand.</p>
      <div class="lists">
        <div>
          <h3>RESIDENTIAL CLEANING</h3>
          <ul><li>General house cleaning</li><li>Home help</li><li>Rental vacancies</li><li>Post renovation cleans</li></ul>
        </div>
        <div>
          <h3>COMMERCIAL CLEANING</h3>
          <ul><li>Business Premises</li><li>Vacated properties</li><li>Schools</li><li>Motels/Hotels</li></ul>
        </div>
      </div>
    </div>
  </section>

</body>
</html>
```